Webdesign für Testportal für Verbraucher
Zielgruppe
Wir bieten ein Testportal für Verbraucher an, die sich vor einer Kaufentscheidung umfassend informieren wollen.
Das Testportal beschränkt sich nicht auf bestimmte Produktgruppen, sondern wird in Zukunft Stück für Stück erweitert. Wir beginnen mit Werkzeugen und erweitern dann andere Kategorien. Zielgruppe sind Personen im mittleren Alter (30 - 55 J m/w).
Aufgabenstellung
Ein Logo ist bereits vorhanden.
Gestyled werden soll der Produkttest. Dieser besteht aus verschiedenen Komponenten:
Bilder, ein Testvideo, ein langer Testbericht, einem Inhaltsverzeichnis (sticky, wie hier: https://www.kaufkompass-beispiel.de/test/das-beste-smartphone/), Informationen über den Autor, Hinweise zur Vorgehensweise mit Icons und Kundenmeinungen (Zitat, Bild, Bewertungssterne), grafische Darstellung des Fazits (Punkteskala) mit Vor- und Nachteilen.
Außerdem soll ein Header mit Navi designed werden.
Das Schriftbild sollte schön übersichtlich sein, wie beispielsweise hier:
https://www.gerätelotse-beispiel.de/schraubstock-test/
Es sollte nicht so überladen wirken wie hier:
https://www.kaufkompass-beispiel.de/test/das-beste-smartphone/
Besonders wichtig ist uns auch die Mobile-Ansicht.
Für die Entwürfe können Stock-Fotos verwendet werden, wir werden diese später durch eigene Bilder ersetzen.
Farblich sind wir nicht gebunden.

```html
<!DOCTYPE html>
<html lang="de">
<head>
<meta charset="utf-8">
<title>prüfwerk.org – Schraubstock-Test</title>
<link rel="stylesheet" href="https://fonts.googleapis.com/css2?family=Roboto:ital,wght@0,300;0,400;0,500;0,700;1,400&display=swap">
<style>
:root{
  --blue:#1f5fb5;
  --blue-dark:#174c93;
  --blue-soft:#e8eef8;
  --ink:#222631;
  --text:#555a63;
  --muted:#9499a2;
  --line:#e3e5e8;
  --page:#f3f4f6;
  --panel:#ffffff;
  --box:#e6e7e9;
  --footer:#1f2230;
  --star:#f5b301;
  --green:#2fb34a;
  --red:#e2413a;
}
*{box-sizing:border-box;margin:0;padding:0}
html,body{width:1200px;height:4872px;overflow:hidden}
body{font-family:"Roboto",Arial,sans-serif;background:var(--page);color:var(--ink);position:relative}
a{color:inherit;text-decoration:none}
ul,ol{list-style:none}

/* header */
.site-header{position:absolute;left:0;top:0;width:1200px;height:62px;background:#fff;border-bottom:3px solid var(--blue)}
.brand{position:absolute;left:218px;top:14px;display:flex;align-items:center;gap:8px;font-size:24px;font-weight:500;color:var(--ink)}
.brand-dot{width:16px;height:16px;border:2px solid var(--ink)}
.main-nav{position:absolute;left:642px;top:20px;display:flex;font-size:13px;color:#3a3e47}
.main-nav a{margin-right:22px;display:flex;align-items:center;gap:5px}
.nav-search{position:absolute;left:958px;top:19px}

/* content panel */
.content-panel{position:absolute;left:76px;top:100px;width:1009px;height:3525px;background:var(--panel)}

/* test article */
.test-article{position:absolute;left:220px;top:151px;width:500px}
.post-date{font-size:11px;color:var(--blue);letter-spacing:.3px;margin-bottom:8px}
.test-title{font-size:20px;font-weight:700;line-height:27px;color:var(--ink)}
.post-meta{display:flex;align-items:center;gap:5px;font-size:8px;color:#555;letter-spacing:.4px;text-transform:uppercase;margin-top:8px}
.media{width:500px;height:298px;margin-top:18px}
.lead{font-size:11px;line-height:18px;color:var(--text);margin-top:14px}
.section-title{font-size:15px;font-weight:700;line-height:20px;color:var(--ink);margin:34px 0 10px;padding-left:10px;border-left:3px solid var(--blue)}
.sub-title{font-size:13px;font-weight:500;color:var(--ink);margin:18px 0 6px}
.body-text{font-size:11px;line-height:18px;color:var(--text)}
.body-text + .body-text{margin-top:10px}
.caption{font-size:9px;color:var(--muted);margin-top:6px}

.video{position:relative;width:500px;height:282px;background:linear-gradient(180deg,#cfd3d8,#9ca3ab 55%,#5f666e)}
.video svg{position:absolute;left:218px;top:109px}

.gallery{display:flex;gap:12px;margin-top:16px}
.gallery div{flex:1;height:150px}

.quote-box{position:relative;width:500px;height:188px;background:var(--box);border-left:5px solid var(--blue-dark);margin-top:26px}
.quote-box .open{position:absolute;left:20px;top:14px;font-size:64px;font-weight:700;color:var(--blue-dark);line-height:1;font-family:Georgia,serif}
.quote-box .close{position:absolute;left:362px;top:118px;font-size:64px;font-weight:700;color:var(--blue-dark);line-height:1;font-family:Georgia,serif}
.quote-box blockquote{position:absolute;left:60px;top:36px;width:380px;text-align:center;font-size:16px;line-height:23px;font-weight:300;color:#2b2f38}
.quote-box cite{position:absolute;left:400px;top:156px;font-size:13px;color:var(--blue);font-style:italic}

.steps{display:grid;grid-template-columns:1fr 1fr;gap:14px}
.step{display:flex;gap:12px;background:#f5f6f8;padding:14px;height:86px}
.step-icon{width:36px;height:36px;border-radius:50%;background:var(--blue);flex:none;display:flex;align-items:center;justify-content:center}
.step h4{font-size:11px;font-weight:500;margin-bottom:4px}
.step p{font-size:9.5px;line-height:15px;color:var(--text)}

.link-box{position:relative;width:500px;height:110px;background:var(--box);border-left:5px solid var(--blue-dark);margin-top:14px}
.link-box .url{position:absolute;left:16px;top:42px;font-size:20px;font-weight:700;color:#1e2230;letter-spacing:.3px}
.link-box svg{position:absolute;right:10px;top:12px}

.score{display:flex;gap:26px;align-items:center;border:1px solid var(--line);padding:22px 24px}
.score-total{width:120px;flex:none;text-align:center}
.score-total strong{display:block;font-size:11px;font-weight:500;color:var(--ink);margin-top:6px}
.score-bars{flex:1}
.bar{display:flex;align-items:center;gap:10px;height:24px;font-size:10px;color:var(--text)}
.bar span:first-child{width:92px}
.bar .track{flex:1;height:6px;background:var(--line);position:relative}
.bar .track i{position:absolute;left:0;top:0;height:6px;background:var(--blue)}
.bar b{width:24px;text-align:right;font-weight:500;color:var(--ink)}

.proscons{width:505px;height:252px;border:1px solid var(--line);display:flex;margin-top:18px}
.proscons .col{flex:1;border-right:1px solid var(--line)}
.proscons .col:last-child{border-right:0}
.proscons h3{height:46px;background:#f0f1f3;display:flex;align-items:center;gap:8px;padding-left:12px;font-size:14px;font-weight:400;color:#333;border-bottom:1px solid var(--line)}
.proscons ul{padding:22px 0 0 18px}
.proscons li{font-size:11px;color:var(--muted);height:33px;position:relative;padding-left:16px;font-weight:300}
.proscons li::before{content:"";position:absolute;left:0;top:6px;width:4px;height:4px;border-radius:50%;background:#c9ccd1}

.author{display:flex;gap:18px;background:#f5f6f8;padding:20px;margin-top:30px;border-top:3px solid var(--blue)}
.author-photo{width:70px;height:70px;border-radius:50%;background:linear-gradient(135deg,#b8bec7,#7d8591);flex:none}
.author small{font-size:9px;color:var(--blue);letter-spacing:.5px;text-transform:uppercase}
.author h4{font-size:14px;font-weight:700;margin:3px 0 6px}
.author p{font-size:10.5px;line-height:17px;color:var(--text)}

/* sidebar */
.sidebar{position:absolute;left:738px;top:170px;width:241px}
.search-widget{height:80px;background:#eeeff1;padding:20px 14px 0}
.search-widget label{display:block;font-size:10px;font-weight:500;color:#333;margin-bottom:6px}
.search-field{height:26px;background:#fff;display:flex;align-items:center;justify-content:space-between;padding:0 10px;font-size:9px;color:#666}
.widget-title{font-size:12px;font-weight:500;color:var(--blue);letter-spacing:.3px;padding-bottom:8px;border-bottom:2px solid var(--blue);margin:32px 0 14px}
.toc{position:sticky;top:20px;background:var(--blue-soft);padding:4px 14px 10px;margin-top:32px}
.toc .widget-title{margin:12px 0 6px}
.toc li{height:27px;display:flex;align-items:center;gap:8px;font-size:10px;color:#333;border-bottom:1px solid #d5dfee}
.toc li:last-child{border-bottom:0}
.toc li b{width:18px;font-weight:500;color:var(--blue)}
.toc li.active{color:var(--blue);font-weight:500}
.tags{display:flex;flex-wrap:wrap;gap:12px 12px}
.tag{height:27px;background:#eeeff1;font-size:8px;color:#333;display:flex;align-items:center;padding:0 13px}
.recent-item{padding:0 0 14px;margin-bottom:14px;border-bottom:1px solid var(--line)}
.recent-item h4{font-size:11px;font-weight:500;margin-bottom:8px}
.recent-body{display:flex;gap:13px}
.recent-thumb{width:51px;height:51px;background:#c9cacc;flex:none}
.recent-body p{font-size:8px;line-height:17px;color:#555}
.cats li{height:29px;border-bottom:1px solid var(--line);font-size:9px;font-weight:500;color:var(--blue);display:flex;align-items:center}

/* pagination */
.pagination{position:absolute;left:500px;top:3688px;display:flex;gap:8px;align-items:center;font-size:10px;color:#333}
.pagination span{width:28px;height:28px;display:flex;align-items:center;justify-content:center}
.pagination .current{background:#fff;border-bottom:2px solid #ccc}

/* testimonials */
.testimonials-title{position:absolute;left:0;top:3790px;width:1200px;text-align:center;font-size:24px;font-weight:300;color:#333}
.testimonials-title strong{font-weight:700;color:var(--ink)}
.testimonials-sub{position:absolute;left:350px;top:3826px;width:500px;text-align:center;font-size:9px;line-height:15px;color:#888}
.t-card{position:absolute;top:3892px;width:246px;height:170px;background:#fff;box-shadow:0 2px 10px rgba(0,0,0,.06);padding:20px 20px 0}
.t-card.faded{opacity:.25}
.t-head{display:flex;gap:10px;align-items:center}
.t-avatar{width:42px;height:42px;border-radius:50%;background:linear-gradient(135deg,#c08a4a,#6b4a2c);flex:none}
.t-name{font-size:11px;color:var(--blue);font-weight:500}
.t-role{font-size:8px;color:#888;margin-top:3px}
.t-text{font-size:8.5px;font-style:italic;line-height:14px;color:#444;margin-top:14px}
.t-stars{color:var(--star);font-size:11px;letter-spacing:2px;margin-top:12px}
.t-arrow{position:absolute;top:3965px}
.dots{position:absolute;left:533px;top:4116px;display:flex;gap:6px}
.dots span{width:22px;height:3px;background:#d8dadd}
.dots .on{width:32px;background:var(--blue)}

/* contact band */
.contact-band{position:absolute;left:0;top:4172px;width:1200px;height:481px;background:var(--blue)}
.contact-band h2{position:absolute;left:240px;top:52px;width:720px;text-align:center;color:#fff;font-size:17px;font-weight:700;line-height:27px}
.field{position:absolute;height:30px;background:#fff;font-size:9px;color:#555;padding:9px 20px}
.field.area{height:75px}
.send{position:absolute;left:808px;top:388px;width:106px;height:30px;background:#fff;color:var(--blue);font-size:10px;font-weight:700;display:flex;align-items:center;justify-content:center;letter-spacing:.5px}

/* footer */
.site-footer{position:absolute;left:0;top:4653px;width:1200px;height:219px;background:var(--footer);color:#fff}
.f-col{position:absolute;top:45px}
.f-col h4{font-size:11px;font-weight:500;margin-bottom:20px}
.f-col li{font-size:10px;height:20px;display:flex;align-items:center;gap:12px;color:#e6e7ea}
.f-brand{position:absolute;left:752px;top:62px;display:flex;align-items:center;gap:14px;font-size:44px;font-weight:500;line-height:1}
.f-brand i{width:40px;height:40px;border:3px solid #fff;display:block}
.copyright{position:absolute;left:0;top:195px;width:1200px;text-align:center;font-size:9px;color:#9a9ca6}
</style>
</head>
<body>

<header class="site-header">
  <a class="brand" href="#"><span class="brand-dot"></span>prüfwerk.org</a>
  <nav class="main-nav">
    <a href="#">Startseite</a>
    <a href="#">Über uns</a>
    <a href="#">Kategorien <svg width="8" height="6" viewBox="0 0 8 6"><path d="M1 1l3 3 3-3" stroke="#3a3e47" stroke-width="1.3" fill="none"/></svg></a>
    <a href="#">Kontakt</a>
  </nav>
  <svg class="nav-search" width="14" height="14" viewBox="0 0 14 14"><circle cx="6" cy="6" r="4.2" stroke="#1f5fb5" stroke-width="1.8" fill="none"/><path d="M9 9l3.5 3.5" stroke="#1f5fb5" stroke-width="1.8"/></svg>
</header>

<main class="content-panel"></main>

<article class="test-article">
  <div class="post-date">08.10.2018</div>
  <h1 class="test-title">Schraubstock-Test: Die besten Modelle für Werkstatt und Hobby im Vergleich</h1>
  <div class="post-meta"><svg width="10" height="10" viewBox="0 0 10 10"><rect x="1" y="1" width="8" height="8" fill="none" stroke="#555"/></svg>By Jonas Feldner &nbsp;/&nbsp; 340 Views &nbsp;/&nbsp; Lesezeit 8 Min.</div>
  <div class="media" role="img" aria-label="Produktfoto: Schraubstock auf einer Werkbank" style="background:linear-gradient(120deg,#e9ebee,#bfc4ca 45%,#5d6168 72%,#c9b39a)"></div>
  <p class="lead">Ein guter Schraubstock hält Werkstücke sicher, lässt sich leicht bedienen und übersteht viele Jahre Einsatz. Wir haben aktuelle Modelle über mehrere Wochen geprüft und zeigen, worauf es beim Kauf wirklich ankommt.</p>

  <h2 class="section-title" id="video">Testvideo</h2>
  <div class="video" role="img" aria-label="Video-Vorschau: Schraubstock im Praxistest">
    <svg width="64" height="64" viewBox="0 0 64 64"><circle cx="32" cy="32" r="32" fill="#2a2a2a"/><path d="M25 19l20 13-20 13z" fill="#fff"/></svg>
  </div>
  <p class="caption">Alle Modelle im Praxistest – Spannen, Drehen und Belasten (4:12 Min.)</p>

  <h2 class="section-title" id="bericht">Testbericht</h2>
  <p class="body-text">Im Test mussten die Schraubstöcke Holz, Rohre und Flachstahl sicher halten. Dabei haben wir Spannkraft, Verarbeitung, Handhabung und die Ausstattung der einzelnen Modelle genau verglichen und dokumentiert.</p>
  <h3 class="sub-title">Verarbeitung und Material</h3>
  <p class="body-text">Gusseisen und Stahl sorgen für Stabilität. Gute Modelle laufen spielfrei, die Spindel ist sauber gefertigt und die Backen sitzen parallel. Billige Geräte zeigen hier schnell Schwächen und wackeln unter Last.</p>
  <h3 class="sub-title">Handhabung im Alltag</h3>
  <p class="body-text">Ein drehbarer Fuß und eine leichtgängige Kurbel erleichtern die Arbeit deutlich. Schutzbacken verhindern Kratzer an empfindlichen Werkstücken und gehören bei den besten Geräten bereits zum Lieferumfang.</p>
  <div class="gallery">
    <div role="img" aria-label="Foto: Spannbacken in Nahaufnahme" style="background:linear-gradient(135deg,#8c939c,#3f444b)"></div>
    <div role="img" aria-label="Foto: Schraubstock mit eingespanntem Rohr" style="background:linear-gradient(135deg,#c9ced4,#6c737c)"></div>
  </div>

  <div class="quote-box">
    <span class="open">“</span>
    <blockquote>Ein Schraubstock ist wie ein zweites Paar Hände. Wer hier spart, merkt es bei jedem Werkstück aufs Neue.</blockquote>
    <span class="close">”</span>
    <cite>Marie Vogt</cite>
  </div>

  <h2 class="section-title" id="vorgehen">So haben wir getestet</h2>
  <div class="steps">
    <div class="step"><div class="step-icon"><svg width="16" height="16" viewBox="0 0 14 14"><circle cx="6" cy="6" r="4.2" stroke="#fff" stroke-width="1.8" fill="none"/><path d="M9 9l3.5 3.5" stroke="#fff" stroke-width="1.8"/></svg></div><div><h4>1. Auswahl</h4><p>Wir wählen beliebte Modelle aller Preisklassen aus dem Handel aus.</p></div></div>
    <div class="step"><div class="step-icon"><svg width="16" height="16" viewBox="0 0 16 16"><circle cx="8" cy="8" r="6" stroke="#fff" stroke-width="1.6" fill="none"/><path d="M8 4.5V8l2.5 1.5" stroke="#fff" stroke-width="1.6" fill="none"/></svg></div><div><h4>2. Praxistest</h4><p>Jedes Gerät wird mehrere Wochen im echten Werkstattalltag genutzt.</p></div></div>
    <div class="step"><div class="step-icon"><svg width="16" height="16" viewBox="0 0 16 16"><path d="M3 8.5l3 3 7-7" stroke="#fff" stroke-width="2" fill="none"/></svg></div><div><h4>3. Bewertung</h4><p>Feste Kriterien sorgen für faire und vergleichbare Ergebnisse.</p></div></div>
    <div class="step"><div class="step-icon"><svg width="16" height="16" viewBox="0 0 16 16"><path d="M8 1.5l2 4.2 4.5.6-3.3 3.1.8 4.5L8 11.7l-4 2.2.8-4.5L1.5 6.3l4.5-.6z" fill="#fff"/></svg></div><div><h4>4. Fazit</h4><p>Am Ende steht eine klare Empfehlung für jeden Bedarf.</p></div></div>
  </div>
  <p class="body-text" style="margin-top:18px">Alle Preise und Angebote zum Testsieger finden Sie direkt beim Händler:</p>
  <div class="link-box">
    <svg width="18" height="18" viewBox="0 0 18 18"><path d="M7.5 10.5l3-3M6 8.5L4 10.5a2.8 2.8 0 004 4l2-2M12 9.5l2-2a2.8 2.8 0 00-4-4l-2 2" stroke="#1f5fb5" stroke-width="1.8" fill="none" stroke-linecap="round"/></svg>
    <div class="url">https://www.beispielklick.de/</div>
  </div>

  <h2 class="section-title" id="fazit">Fazit</h2>
  <div class="score">
    <div class="score-total">
      <svg width="96" height="96" viewBox="0 0 96 96"><circle cx="48" cy="48" r="40" stroke="#e3e5e8" stroke-width="8" fill="none"/><circle cx="48" cy="48" r="40" stroke="#1f5fb5" stroke-width="8" fill="none" stroke-dasharray="216 251" transform="rotate(-90 48 48)"/><text x="48" y="53" text-anchor="middle" font-family="Roboto,Arial,sans-serif" font-size="22" font-weight="700" fill="#222631">8,6</text><text x="48" y="68" text-anchor="middle" font-family="Roboto,Arial,sans-serif" font-size="9" fill="#9499a2">von 10</text></svg>
      <strong>Sehr gut</strong>
    </div>
    <div class="score-bars">
      <div class="bar"><span>Verarbeitung</span><span class="track"><i style="width:90%"></i></span><b>9,0</b></div>
      <div class="bar"><span>Spannkraft</span><span class="track"><i style="width:85%"></i></span><b>8,5</b></div>
      <div class="bar"><span>Handhabung</span><span class="track"><i style="width:80%"></i></span><b>8,0</b></div>
      <div class="bar"><span>Ausstattung</span><span class="track"><i style="width:75%"></i></span><b>7,5</b></div>
      <div class="bar"><span>Preis-Leistung</span><span class="track"><i style="width:92%"></i></span><b>9,2</b></div>
    </div>
  </div>

  <section class="proscons">
    <div class="col">
      <h3><svg width="16" height="16" viewBox="0 0 16 16"><circle cx="8" cy="8" r="8" fill="#2fb34a"/><path d="M4.5 8.2l2.3 2.3 4.7-4.8" stroke="#fff" stroke-width="1.8" fill="none"/></svg>Vorteile</h3>
      <ul>
        <li>Gleichmäßige Spannkraft</li>
        <li>Für kleine und große Werkstücke</li>
        <li>Vielseitig einsetzbar</li>
        <li>Breites Angebot</li>
        <li>Günstig zu erhalten</li>
      </ul>
    </div>
    <div class="col">
      <h3><svg width="16" height="16" viewBox="0 0 16 16"><circle cx="8" cy="8" r="8" fill="#e2413a"/><path d="M5.3 5.3l5.4 5.4M10.7 5.3l-5.4 5.4" stroke="#fff" stroke-width="1.8"/></svg>Nachteile</h3>
      <ul>
        <li>Für spezielle Anforderungen nicht ideal</li>
      </ul>
    </div>
  </section>

  <div class="author" id="autor">
    <div class="author-photo" role="img" aria-label="Autorenfoto"></div>
    <div>
      <small>Über den Autor</small>
      <h4>Jonas Feldner</h4>
      <p>Schreinermeister und Redakteur für Werkzeuge. Seit über zehn Jahren testet er Geräte für Werkstatt und Heimwerker und erklärt, was im Alltag wirklich zählt.</p>
    </div>
  </div>
</article>

<aside class="sidebar">
  <div class="search-widget">
    <label>Suche</label>
    <div class="search-field">Geben Sie Ihr Schlüsselwort ein
      <svg width="11" height="11" viewBox="0 0 14 14"><circle cx="6" cy="6" r="4.2" stroke="#333" stroke-width="2" fill="none"/><path d="M9 9l3.5 3.5" stroke="#333" stroke-width="2"/></svg>
    </div>
  </div>

  <nav class="toc">
    <h3 class="widget-title">INHALTSVERZEICHNIS</h3>
    <ol>
      <li class="active"><b>01</b>Einleitung</li>
      <li><b>02</b>Testvideo</li>
      <li><b>03</b>Testbericht</li>
      <li><b>04</b>So haben wir getestet</li>
      <li><b>05</b>Fazit und Bewertung</li>
      <li><b>06</b>Vor- und Nachteile</li>
      <li><b>07</b>Über den Autor</li>
      <li><b>08</b>Kundenmeinungen</li>
    </ol>
  </nav>

  <h3 class="widget-title">BELIEBTE TAGS</h3>
  <div class="tags">
    <span class="tag">Verwaltung</span><span class="tag">SEO</span><span class="tag" style="padding:0 30px">Beirat</span>
    <span class="tag">Soft Skills</span><span class="tag">Handy, Mobiltelefon</span><span class="tag">Spiele</span>
  </div>

  <h3 class="widget-title">LETZTER BEITRAG</h3>
  <div class="recent-item"><h4>Lorem ipsum</h4><div class="recent-body"><div class="recent-thumb" role="img" aria-label="Beitragsbild"></div><p>Ut enim ad minim veniam, quis nostrud no laboris nisi ut aliquip ex ea commodo consequat. Duis aute irure</p></div></div>
  <div class="recent-item"><h4>Lorem ipsum</h4><div class="recent-body"><div class="recent-thumb" role="img" aria-label="Beitragsbild"></div><p>Ut enim ad minim veniam, quis nostrud no laboris nisi ut aliquip ex ea commodo consequat. Duis aute irure</p></div></div>
  <div class="recent-item"><h4>Lorem ipsum</h4><div class="recent-body"><div class="recent-thumb" role="img" aria-label="Beitragsbild"></div><p>Ut enim ad minim veniam, quis nostrud no laboris nisi ut aliquip ex ea commodo consequat. Duis aute irure</p></div></div>

  <h3 class="widget-title">KATEGORIEN</h3>
  <ul class="cats">
    <li>›&nbsp;&nbsp;The Lorem Ipsum (16)</li>
    <li>›&nbsp;&nbsp;The Lorem Ipsum (8)</li>
    <li>›&nbsp;&nbsp;The Lorem Ipsum</li>
    <li>›&nbsp;&nbsp;The Lorem Ipsum</li>
    <li>›&nbsp;&nbsp;The Lorem Ipsum</li>
  </ul>
</aside>

<nav class="pagination">
  <span>‹</span><span class="current">1</span><span>2</span><span>3</span><span>›</span>
</nav>

<h2 class="testimonials-title">Was ist unser <strong>Kunden</strong> sagen</h2>
<p class="testimonials-sub">Lorem ipsum dolor sit amet, consectetur adipiscing elit, sed do eiusmod tempor incididunt ut labore et dolore magna aliqua. Ut enim ad minim veniam, quis nostrud exercitation.</p>

<div class="t-card faded" style="left:-85px">
  <div class="t-head"><div class="t-avatar" role="img" aria-label="Kundenfoto"></div><div><div class="t-name">Nils Hagen</div><div class="t-role">Design Partner</div></div></div>
  <p class="t-text">Wir schätzen die klare Aufbereitung, die jeden Vergleich auf den Punkt bringt und Entscheidungen leicht macht.</p>
  <div class="t-stars">★★★★★</div>
</div>
<svg class="t-arrow" style="left:136px" width="28" height="10" viewBox="0 0 28 10"><path d="M27 5H2M6 1L2 5l4 4" stroke="#222" stroke-width="1.4" fill="none"/></svg>

<div class="t-card" style="left:189px">
  <div class="t-head"><div class="t-avatar" role="img" aria-label="Kundenfoto"></div><div><div class="t-name">Lena Brandt</div><div class="t-role">Grafikdesignerin</div></div></div>
  <p class="t-text">Die Testberichte sind klar gegliedert, ehrlich geschrieben und helfen mir wirklich bei jeder Kaufentscheidung.</p>
  <div class="t-stars">★★★★★</div>
</div>
<div class="t-card" style="left:456px">
  <div class="t-head"><div class="t-avatar" role="img" aria-label="Kundenfoto" style="background:linear-gradient(135deg,#6b6f78,#2d3038)"></div><div><div class="t-name">Tobias Kern</div><div class="t-role">Webentwickler</div></div></div>
  <p class="t-text">Übersichtliche Vergleiche, verständliche Fazits und eine Bewertung, der man vertrauen kann. Sehr empfehlenswert.</p>
  <div class="t-stars">★★★★★</div>
</div>
<div class="t-card" style="left:723px">
  <div class="t-head"><div class="t-avatar" role="img" aria-label="Kundenfoto" style="background:linear-gradient(135deg,#c2362f,#5a1c1a)"></div><div><div class="t-name">Sofia Lindner</div><div class="t-role">Icon-Designerin</div></div></div>
  <p class="t-text">Endlich ein Portal, das Vor- und Nachteile ohne Umwege zeigt. Ich spare viel Zeit bei der Recherche.</p>
  <div class="t-stars">★★★★★</div>
</div>

<svg class="t-arrow" style="left:996px" width="28" height="10" viewBox="0 0 28 10"><path d="M1 5h25M22 1l4 4-4 4" stroke="#222" stroke-width="1.4" fill="none"/></svg>
<div class="t-card faded" style="left:1040px">
  <div class="t-head"><div class="t-avatar" role="img" aria-label="Kundenfoto" style="background:#cfd2d6"></div><div><div class="t-name">Paula Wendt</div><div class="t-role">Illustratorin</div></div></div>
  <p class="t-text">Gute Übersicht, faire Punkte und verständliche Texte. So macht Vergleichen wirklich Spaß.</p>
  <div class="t-stars">★★★★★</div>
</div>
<div class="dots"><span></span><span class="on"></span><span></span></div>

<section class="contact-band">
  <h2>Benötigen Sie Hilfe bei Ihrer PR? Wir bauen den Ruf unserer Marke auf, bieten echte Lösungen für geschäftliche Herausforderungen und tun alles, um die Ergebnisse zu erzielen, die Sie verdienen. Wir würden gerne von Ihnen hören.</h2>
  <div class="field" style="left:286px;top:176px;width:303px">Vorname*</div>
  <div class="field" style="left:610px;top:176px;width:304px">Email*</div>
  <div class="field" style="left:286px;top:225px;width:303px">Nachname*</div>
  <div class="field" style="left:610px;top:225px;width:304px">Telefon</div>
  <div class="field area" style="left:286px;top:275px;width:628px">Schreiben Sie ihre Nachricht hier</div>
  <div class="send">SENDEN</div>
</section>

<footer class="site-footer">
  <div class="f-col" style="left:220px">
    <h4>Kontaktiere uns</h4>
    <ul>
      <li><svg width="9" height="11" viewBox="0 0 9 11"><path d="M4.5 10.5S8 6.5 8 4a3.5 3.5 0 00-7 0c0 2.5 3.5 6.5 3.5 6.5z" fill="#fff"/><circle cx="4.5" cy="4" r="1.3" fill="#1f2230"/></svg>Lindenweg 12</li>
      <li><svg width="10" height="10" viewBox="0 0 10 10"><path d="M2 1l2 2-1 1.5a6 6 0 002.5 2.5L7 6l2 2-1.5 1.5C4 9 1 6 .5 2.5z" fill="#fff"/></svg>0351-448-2170</li>
      <li><svg width="10" height="8" viewBox="0 0 10 8"><rect width="10" height="8" fill="#fff"/><path d="M0 0l5 4 5-4" stroke="#1f2230" fill="none"/></svg>info@pruefwerk-beispiel.de</li>
    </ul>
  </div>
  <div class="f-col" style="left:416px">
    <h4>Nützliche Links</h4>
    <ul>
      <li>›&nbsp;Startseite</li>
      <li>›&nbsp;Über uns</li>
      <li>›&nbsp;Kategorien</li>
      <li>›&nbsp;Kontakt</li>
    </ul>
  </div>
  <div class="f-brand"><i></i>prüfwerk</div>
  <p class="copyright">© All Rights Reserved.</p>
</footer>

</body>
</html>
```